Central Florida Lawn and Landscape business needs an awesome flyer design!

We are a growing lawn and landscape maintenance business looking to incorporate print mail for target advertising. This project should provide some editing capabilities for us to incorporate our logo, update any promotional offers, and adjust throughout the various seasons (lawn service, mulch jobs, one-time clean-ups, hardscape projects, etc). We'd like a clear call to action (one that we can edit if needed) to call or text today. We'll include our website address as well.
The business name is Velo Grassworks.
Target Market(s)
Residential homeowners
Industry/Entity Type
Lawn and landscape maintenance
Font styles to use
Other font styles liked:
- Couture
Look and feel

```html
<!DOCTYPE html>
<html lang="en">
<head>
<meta charset="UTF-8">
<title>Velo Grassworks – Lawn Service Flyer</title>
<link href="https://fonts.googleapis.com/css2?family=Bebas+Neue&family=Poppins:wght@400;500;600&display=swap" rel="stylesheet">
<style>
  :root{
    --stage:#e6e6e6;
    --forest:#0f4a16;
    --leaf:#1f6b26;
    --moss:#4c8c3a;
    --lime:#b9f27c;
    --ink:#2a2a2a;
    --orange-a:#f7a023;
    --orange-b:#f47a12;
    --paper:#ffffff;
    --paper-fade:#e9e9e9;
  }
  *{margin:0;padding:0;box-sizing:border-box}
  html,body{width:1200px;height:1200px;overflow:hidden;background:var(--stage)}
  .flyer{position:absolute;left:192px;top:72px;width:821px;height:1062px;overflow:hidden;background:var(--paper);font-family:"Poppins",sans-serif}
  .hero-photo{position:absolute;left:0;top:0;width:821px;height:830px;
    background:linear-gradient(180deg,#1d5a22 0%,#2f6d2a 35%,#4f8a3a 58%,#a57c5a 72%,#5b9a3e 100%)}
  .headline{position:absolute;left:56px;top:30px;color:#fff}
  .headline .intro{font-size:34px;font-weight:400;letter-spacing:-0.5px;line-height:1}
  .headline .main{font-family:"Bebas Neue",sans-serif;font-size:70px;line-height:72px;color:var(--lime);margin-top:12px;letter-spacing:1px;
    text-shadow:2px 2px 0 #0c3a10,3px 3px 0 #fff}
  .brand-tab{position:absolute;left:625px;top:0;width:163px;height:153px;background:var(--paper);border-radius:0 0 12px 12px;
    display:flex;flex-direction:column;align-items:center;justify-content:center;gap:10px}
  .brand-tab .dot{width:34px;height:34px;border-radius:50%;background:var(--leaf)}
  .brand-tab .name{font-size:17px;font-weight:600;color:var(--leaf);text-align:center;line-height:1.1}
  .why-panel{position:absolute;left:297px;top:551px;width:524px;height:300px}
  .why-panel .tab{position:absolute;left:0;top:0;width:416px;height:60px;background:#fbfbfb;border-radius:14px 14px 0 0}
  .why-panel .body{position:absolute;left:0;top:38px;width:524px;height:262px;background:linear-gradient(180deg,#fbfbfb,#f1f1f1)}
  .why-title{position:absolute;left:297px;top:572px;width:466px;text-align:center;font-family:"Bebas Neue",sans-serif;font-size:52px;color:var(--ink);line-height:1;letter-spacing:1px}
  .perk{position:absolute;top:649px;width:130px;text-align:center}
  .perk svg{display:block;margin:0 auto}
  .perk p{margin-top:14px;font-size:15px;line-height:23px;color:var(--leaf)}
  .bottom-panel{position:absolute;left:0;top:819px;width:821px;height:243px;background:linear-gradient(180deg,#f3f3f3,var(--paper-fade));border-radius:16px 0 0 0}
  .ribbon{position:absolute;left:0;top:610px}
  .cta-title{position:absolute;left:61px;top:856px;font-family:"Bebas Neue",sans-serif;font-size:50px;color:var(--ink);line-height:1;letter-spacing:0.5px}
  .contact{position:absolute;top:932px}
  .contact .label{font-size:20px;color:var(--ink);line-height:1}
  .contact .value{display:flex;align-items:center;gap:6px;margin-top:16px;font-family:"Bebas Neue",sans-serif;font-size:36px;color:var(--forest);line-height:1;white-space:nowrap}
  .contact-phone{left:61px}
  .contact-web{left:425px}
</style>
</head>
<body>
<main class="flyer">
  <div class="hero-photo" role="img" aria-label="Photo of a lush garden with flowering beds, shade trees and a curving mulch path"></div>

  <header class="headline">
    <p class="intro">Freshen up your lawn with our</p>
    <h1 class="main">Premier Lawn Service<br>&amp; Mulch Jobs</h1>
  </header>

  <div class="brand-tab">
    <span class="dot"></span>
    <span class="name">Velo Grassworks</span>
  </div>

  <div class="why-panel"><div class="tab"></div><div class="body"></div></div>
  <div class="bottom-panel"></div>

  <h2 class="why-title">Why Choose Us?</h2>

  <div class="perk" style="left:302px">
    <svg width="72" height="72" viewBox="0 0 72 72" fill="none" stroke="#1f6b26" stroke-width="1.6"><circle cx="36" cy="36" r="35"/><circle cx="36" cy="32" r="11"/><circle cx="36" cy="32" r="6"/><path d="M29 41l-5 11 6-2 3 5 3-9M43 41l5 11-6-2-3 5-3-9"/></svg>
    <p>Professional<br>&amp; Reliable<br>Service</p>
  </div>
  <div class="perk" style="left:462px">
    <svg width="72" height="72" viewBox="0 0 72 72" fill="none" stroke="#1f6b26" stroke-width="1.6"><circle cx="36" cy="36" r="35"/><path d="M50 21l-8 20-4-6-6-4z"/><path d="M38 35L22 51"/></svg>
    <p>Experienced<br>Technicians</p>
  </div>
  <div class="perk" style="left:618px">
    <svg width="72" height="72" viewBox="0 0 72 72" fill="none" stroke="#1f6b26" stroke-width="1.6"><circle cx="36" cy="36" r="35"/><path d="M17 38h8l10 3h8a3 3 0 010 6H31M17 48h9l12 3 14-7"/><path d="M42 16l2 6 6 2-6 2-2 6-2-6-6-2 6-2z"/><path d="M31 24v4M29 26h4"/></svg>
    <p>Customized<br>Solutions for<br>Every Season</p>
  </div>

  <svg class="ribbon" width="320" height="240" viewBox="0 0 320 240">
    <defs><linearGradient id="ribbonGlow" x1="0" x2="1"><stop offset="0" stop-color="#f47a12"/><stop offset="1" stop-color="#f7a023"/></linearGradient></defs>
    <polygon points="0,109 51,109 51,219 0,219" fill="#4c8c3a"/>
    <polygon points="0,56 301,14 285,44 310,66 0,109 14,84" fill="url(#ribbonGlow)"/>
    <polygon points="39,109 270,72 284,202 56,232" fill="#0f4a16"/>
    <g font-family="Bebas Neue, sans-serif" fill="#fff" text-anchor="middle">
      <text x="150" y="74" font-size="36" transform="rotate(-8 150 62)">LIMITED TIME OFFER</text>
      <text x="156" y="150" font-size="68" transform="rotate(-8 156 126)">10% OFF</text>
      <text x="166" y="190" font-size="40" transform="rotate(-8 166 176)">ALL SERVICES</text>
    </g>
  </svg>

  <h2 class="cta-title">Ready to transform your outdoors?</h2>

  <div class="contact contact-phone">
    <p class="label">Call or Text Us Today!</p>
    <p class="value">
      <svg width="22" height="24" viewBox="0 0 24 24"><path fill="#1f6b26" d="M6.6 2.5l3 3.5-2 2.5c1 2.5 3.2 4.8 5.8 6l2.4-2 3.6 3-1.8 3.5C10.5 19 4.8 13.3 3.2 6.2z"/></svg>
      [Your Phone Number]
    </p>
  </div>
  <div class="contact contact-web">
    <p class="label">Visit Us Online:</p>
    <p class="value">
      <svg width="19" height="19" viewBox="0 0 20 20" fill="none" stroke="#1f6b26" stroke-width="2"><circle cx="10" cy="10" r="8"/><path d="M2 10h16M10 2c3 3 3 13 0 16M10 2c-3 3-3 13 0 16"/></svg>
      [Your Website Address]
    </p>
  </div>
</main>
</body>
</html>
```